Corvalt Web design

I described what I need to the doc.
Please see the my request from the following URL.
http://marblefox204.tundo.jp/CorvaltHPdraft.pdf

Please see my request and don't suggest boring typical web.

We need the innovation and the unique suggestion from you.

The log updated the site. 

Please see and design on your mind.

Thanks
corvalt

The flag on countries are for changing language.
It must be small, all designs are big.

Seeing the logo image, the we must be cool with white/black/grey.
Most designs are colorful or for kids.

```html
<!DOCTYPE html>
<html lang="en">
<head>
<meta charset="utf-8">
<title>Corvalt</title>
<link rel="stylesheet" href="https://fonts.googleapis.com/css2?family=PT+Sans:wght@400;700&display=swap">
<style>
  :root {
    --bg: #1b1b1b;
    --bg-deep: #111111;
    --band: #2a2a2a;
    --band-glow: #3a3a3a;
    --frame: #4a4a4a;
    --panel: #0a0a0a;
    --panel-border: #3c3c3c;
    --text: #ffffff;
    --text-soft: #c9c9c9;
    --logo: #9a9a9a;
    --btn-top: #ffffff;
    --btn-bottom: #bdbdbd;
    --btn-text: #444444;
    --social: #5a5a5a;
    --photo-a: #d9dde0;
    --photo-b: #8f939a;
  }
  * { box-sizing: border-box; margin: 0; padding: 0; }
  html, body { width: 1200px; height: 878px; overflow: hidden; }
  body {
    position: relative;
    background: radial-gradient(ellipse at 50% 45%, #262626 0%, var(--bg) 55%, var(--bg-deep) 100%);
    font-family: Arial, Helvetica, sans-serif;
    color: var(--text);
  }
  .site-header {
    position: absolute; left: 0; top: 0; width: 1200px; height: 155px;
    background: linear-gradient(180deg, #161616 0%, #222 55%, var(--band-glow) 82%, #1a1a1a 100%);
  }
  .brand {
    position: absolute; left: 340px; top: 42px; height: 90px;
    display: flex; align-items: center; gap: 18px;
  }
  .brand-mark { width: 72px; height: 72px; border-radius: 50%; background: var(--logo); }
  .brand-name {
    font-family: "PT Sans", sans-serif; font-weight: 400;
    font-size: 92px; line-height: 1; color: var(--logo); letter-spacing: -1px;
  }
  .social { position: absolute; display: flex; gap: 8px; z-index: 2; }
  .social-link {
    display: flex; align-items: center; justify-content: center;
    background: var(--social); color: var(--text);
    font-family: "PT Sans", sans-serif; text-decoration: none; white-space: nowrap;
  }
  .social--header { right: 28px; top: 30px; }
  .social--header .social-link { height: 38px; padding: 0 8px; font-size: 13px; }
  .social--footer { left: 50%; transform: translateX(-50%); top: 775px; gap: 4px; }
  .social--footer .social-link { height: 22px; padding: 0 5px; font-size: 10px; line-height: 1; }

  .slider-frame {
    position: absolute; left: 38px; top: 192px; width: 572px; height: 379px;
    background: var(--frame);
  }
  .slide-photo {
    position: absolute; left: 11px; top: 12px; width: 550px; height: 355px;
    background: linear-gradient(135deg, var(--photo-a) 0%, #c3c6c9 45%, var(--photo-b) 100%);
  }
  .slider-arrow { position: absolute; top: 366px; width: 20px; height: 26px; }
  .slider-arrow--prev { left: 12px; }
  .slider-arrow--next { left: 612px; }

  .about-panel {
    position: absolute; left: 640px; top: 192px; width: 540px; height: 380px;
    background: var(--panel); border: 1px solid var(--panel-border);
    padding: 48px 4px 0 36px;
  }
  .about-title { font-size: 29px; font-weight: 400; line-height: 1; margin-bottom: 18px; }
  .about-text { font-size: 15px; line-height: 29px; color: var(--text-soft); }

  .nav-button {
    position: absolute; top: 616px; height: 49px;
    display: flex; align-items: center; justify-content: center;
    background: linear-gradient(180deg, var(--btn-top) 0%, #eeeeee 45%, var(--btn-bottom) 100%);
    border-radius: 3px; box-shadow: 0 6px 8px rgba(0,0,0,.6);
    font-family: "PT Sans", sans-serif; font-size: 30px; color: var(--btn-text);
    text-decoration: none;
  }
  .nav-button--about { left: 121px; width: 216px; }
  .nav-button--services { left: 452px; width: 216px; }
  .nav-button--profile { left: 778px; width: 308px; }

  .site-footer {
    position: absolute; left: 0; top: 790px; width: 1200px; height: 88px; z-index: 1;
    background: linear-gradient(180deg, #2c2c2c 0%, var(--band-glow) 25%, #141414 40%, #121212 100%);
  }
  .copyright {
    position: absolute; left: 0; width: 1200px; top: 836px; text-align: center; z-index: 2;
    font-family: "PT Sans", sans-serif; font-size: 13px; color: #e6e6e6;
  }
</style>
</head>
<body>
  <header class="site-header">
    <div class="brand">
      <span class="brand-mark"></span>
      <span class="brand-name">CORVALT</span>
    </div>
    <nav class="social social--header">
      <a class="social-link" href="#">Chirply</a>
      <a class="social-link" href="#">Friendhub</a>
    </nav>
  </header>

  <section class="slider-frame">
    <div class="slide-photo" role="img" aria-label="Business team seated at a meeting table in a bright office"></div>
  </section>
  <svg class="slider-arrow slider-arrow--prev" viewBox="0 0 20 26"><polyline points="15,3 5,13 15,23" fill="none" stroke="#bfbfbf" stroke-width="3"/></svg>
  <svg class="slider-arrow slider-arrow--next" viewBox="0 0 20 26"><polyline points="5,3 15,13 5,23" fill="none" stroke="#bfbfbf" stroke-width="3"/></svg>

  <section class="about-panel">
    <h2 class="about-title">ABOUT US</h2>
    <p class="about-text">Lorem ipsum dolor sit amet, consectetur adipiscing elit. Aenean placerat porttitor ligula quis fringilla. Vestibulum viverra justo in dui pellentesque convallis. Vivamus ac ligula felis, et bibendum urna. Mauris vitae mauris quis arcu rhoncus auctor ac eu nibh. Vestibulum volutpat justo sit amet nisi auctor vitae rutrum dui porttitor.</p>
  </section>

  <a class="nav-button nav-button--about" href="#">About Us</a>
  <a class="nav-button nav-button--services" href="#">Services</a>
  <a class="nav-button nav-button--profile" href="#">Company Profile</a>

  <footer class="site-footer"></footer>
  <nav class="social social--footer">
    <a class="social-link" href="#">Chirply</a>
    <a class="social-link" href="#">Friendhub</a>
  </nav>
  <p class="copyright">Copyright © 2011. www.corvalt.com</p>
</body>
</html>
```